Fresh Website for PLIM and Qulo alliance

Page designs for 11 pages using existing Tessel template for the homepage and existing company logo.

Mock-up of front page attached, feel free to turn it into something elegant, professional and clean.

Target Market(s)

1. Small to medium business owners who use DRUK or other accounting software who want to use Qulo.
2 Businesses who want to hire a decent Bookkeeper instead of trying to do it on the kitchen table at night.

Industry/Entity Type

It Company

Font styles to use
Sans Serif

Colors
86cae6
32a6d6
34a7d8
cee9f5

Requirements
Must have
• Use the Qulo blue colour for the website theme - PMS: Blue #00A0C6
Use the Tessel template design and theme - pieces of the puzzle all fitting together with Qulo and PLIM
Same font used in the plim blue png uploaded and plimtraining logo
Nice to have
• A style that mirrors and links easily with the Qulo website:
check out www.qulo.com.au
Should not have
• Cheesy pictures of money and $$,
Cluttered feel
Chunky anime like images for buttons icons
Not to scream Tessel and make everything look like a kids website - just subtle nods to the theme

```html
<!DOCTYPE html>
<html lang="en">
<head>
<meta charset="utf-8">
<title>Plim Training</title>
<link rel="stylesheet" href="https://fonts.googleapis.com/css2?family=Open+Sans:wght@300;400;600;700&family=PT+Sans:wght@400;700&display=swap">
<style>
:root{
  --brand:#00a0c6;
  --brand-light:#14b3d9;
  --brand-dark:#0a8fb3;
  --hero-a:#6ccbd9;
  --hero-b:#45b7cb;
  --side-bg:#9fcbd4;
  --side-border:#8dbcc6;
  --text:#333;
  --body-text:#1a1a1a;
  --heading:#2aa2d2;
  --footer:#6b6b6b;
  --footer-text:#dcdcdc;
  --footer-deep:#3d3b3c;
  --field:#3f3d3e;
  --send:#2fa3d6;
  --white:#fff;
}
*{box-sizing:border-box;margin:0;padding:0}
html,body{width:1200px;height:1069px;overflow:hidden;background:var(--white)}
body{position:relative;font-family:"Open Sans",Arial,sans-serif;color:var(--text)}
.top-rule{position:absolute;left:160px;top:13px;width:880px;border-top:1px dashed #bbb}
.logo{position:absolute;left:160px;top:44px;display:flex;align-items:center;gap:9px;white-space:nowrap}
.logo-mark{width:16px;height:16px;background:var(--brand)}
.logo-name{font-family:"PT Sans",sans-serif;font-weight:700;font-size:34px;color:var(--brand);letter-spacing:1px;line-height:1}
.phone{position:absolute;right:160px;top:50px;display:flex;align-items:center;gap:8px;font-size:20px;color:#222;white-space:nowrap}
.nav{position:absolute;left:160px;top:114px;width:880px;height:44px;background:linear-gradient(var(--brand-light),var(--brand));display:flex;justify-content:space-around;align-items:center;padding:0 30px;border-bottom:1px solid var(--brand-dark)}
.nav a{font-family:"PT Sans",sans-serif;font-size:16px;color:var(--white);text-decoration:none;text-transform:uppercase;white-space:nowrap}
.hero{position:absolute;left:160px;top:158px;width:880px;height:330px;background:linear-gradient(135deg,var(--hero-a),var(--hero-b))}
.hero-caption{position:absolute;left:0;top:187px;width:393px;height:81px;background:rgba(60,110,120,.72);border-radius:0 6px 6px 0;padding:10px 14px;font-family:"PT Sans",sans-serif;font-size:25px;line-height:31px;color:var(--white);text-transform:uppercase;white-space:nowrap}
.hero-dots{position:absolute;right:31px;top:297px;display:flex;gap:3px}
.hero-dots span{width:11px;height:11px;border-radius:50%;background:var(--white)}
.hero-dots span.active{background:#444}
.services{position:absolute;left:160px;top:507px;width:274px;height:264px;background:var(--side-bg);border:1px solid var(--side-border);padding:14px 11px}
.service{display:flex;align-items:center;height:43px;margin-bottom:20px;padding-left:18px;border-radius:7px;background:linear-gradient(#fff,#e6e6e6);box-shadow:0 3px 4px rgba(0,0,0,.25);font-family:"PT Sans",sans-serif;font-size:16px;color:#222;text-transform:uppercase}
.welcome{position:absolute;left:468px;top:500px;width:564px}
.welcome h1{font-weight:300;font-size:31px;color:var(--heading);margin-bottom:14px;white-space:nowrap}
.welcome p{font-size:11px;line-height:15px;font-weight:400;color:var(--body-text);text-align:justify;margin-bottom:14px}
.read-more{position:absolute;left:464px;top:732px;width:100px;height:30px;border-radius:6px;background:linear-gradient(#f2f2f2,#d6d6d6);box-shadow:0 2px 3px rgba(0,0,0,.3);font-size:12px;color:#333;display:flex;align-items:center;justify-content:center}
.footer{position:absolute;left:0;top:808px;width:1200px;height:224px;background:var(--footer);color:var(--footer-text)}
.col{position:absolute;top:0;width:220px;height:224px}
.col h2{position:absolute;left:0;top:14px;font-weight:400;font-size:16px;line-height:22px;color:var(--white);text-transform:uppercase;white-space:nowrap}
.col ul{list-style:none;position:absolute;left:0;top:42px;font-size:11.5px;line-height:15px;white-space:nowrap}
.about p{position:absolute;left:0;top:42px;width:210px;font-size:11.5px;line-height:16px}
.share{position:absolute;left:0;top:126px;display:flex;gap:14px}
.share-btn{display:flex;align-items:center;font-size:10px}
.share-btn b{background:#eef1f6;border:1px solid #aab;padding:1px 5px;color:#3b5a99;font-weight:600;display:flex;align-items:center;gap:3px}
.share-btn b i{width:8px;height:8px;background:#3b5a99}
.share-btn span{background:var(--white);color:#333;padding:1px 8px;margin-left:3px}
.field{position:absolute;background:var(--field);color:#eee;font-size:11px;padding:4px 10px;border-radius:2px}
.send{position:absolute;left:798px;top:180px;width:143px;height:24px;background:var(--send);color:var(--white);font-weight:700;font-size:14px;display:flex;align-items:center;justify-content:center;border-bottom:2px solid #555}
.copyright{position:absolute;left:0;top:1032px;width:1200px;height:37px;background:var(--footer-deep);color:#eee;font-size:11.5px;padding:14px 0 0 177px;white-space:nowrap}
</style>
</head>
<body>
<div class="top-rule"></div>

<div class="logo">
  <span class="logo-mark"></span>
  <span class="logo-name">PLIM TRAINING</span>
</div>

<div class="phone">
  <svg width="18" height="20" viewBox="0 0 18 20"><path d="M4 1 L7 1 L8 6 L6 7.5 Q7.5 12 11 14 L12.5 12 L17 13 L17 17 Q16 19 13 18.5 Q3 15 1.5 5 Q1.5 2 4 1Z" fill="#222"/></svg>
  <span>0800 555 019</span>
</div>

<nav class="nav">
  <a>Home</a><a>Learn More</a><a>About</a><a>Free Initial Consult</a><a>Clients</a><a>Blog</a><a>Contact</a>
</nav>

<section class="hero" role="img" aria-label="Photo of a hand drawing interlocking white puzzle-piece outlines on a turquoise background">
  <div class="hero-caption">Unleash the power of Qulo<br>in your business</div>
  <div class="hero-dots"><span class="active"></span><span></span><span></span><span></span><span></span></div>
</section>

<aside class="services">
  <div class="service">Bookkeeping</div>
  <div class="service">Training</div>
  <div class="service">Support</div>
  <div class="service">Set-up</div>
</aside>

<main class="welcome">
  <h1>Welcome to Plim Training</h1>
  <p>Lorem Ipsum is simply dummy text of the printing and typesetting industry. Lorem Ipsum has been the industry's standard dummy text ever since the 1500s, when an unknown printer took a galley of type and scrambled it to make a type specimen book. It has survived not only five centuries,</p>
  <p>but also the leap into electronic typesetting, remaining essentially unchanged. It was popularised in the 1960s with the release of Letterfix sheets containing Lorem Ipsum passages, and more recently with desktop publishing software like Pagewright including versions of Lorem Ipsum.</p>
  <p>but also the leap into electronic typesetting, remaining essentially unchanged. It was popularised in the 1960s with the release of Letterfix sheets containing Lorem Ipsum passages, and more recently with desktop publishing software like Pagewright including versions of Lorem Ipsum.</p>
</main>
<div class="read-more">Read More</div>

<footer class="footer">
  <div class="col about" style="left:175px">
    <h2>About Tessel</h2>
    <p>Maecenas lorem lacus, dapibus ullam corper dignissim non, dictum sed velit. Integer eget enim sit amet diam hendrerit dignissim.</p>
    <div class="share">
      <div class="share-btn"><b><i></i>Like</b><span>9</span></div>
      <div class="share-btn"><b><i></i>Chirp</b><span>1</span></div>
    </div>
  </div>
  <div class="col" style="left:418px;width:140px">
    <h2>Main Menu</h2>
    <ul><li>Home</li><li>Learn more</li><li>About</li><li>Free Initial Consult</li><li>Clients</li><li>Contact</li><li>Blog</li></ul>
  </div>
  <div class="col" style="left:569px;width:140px">
    <h2>Social Media</h2>
    <ul><li>Gatherly</li><li>Chirper</li><li>Circle Plus</li><li>linkwork</li></ul>
  </div>
  <div class="col" style="left:719px;width:140px;height:40px">
    <h2>Contact Us</h2>
  </div>
  <div class="field" style="left:719px;top:44px;width:144px;height:22px">Name</div>
  <div class="field" style="left:873px;top:44px;width:144px;height:22px">Email</div>
  <div class="field" style="left:719px;top:76px;width:298px;height:87px">Your question</div>
  <div class="send">SEND</div>
</footer>

<div class="copyright">Copyright 2014 · All rights reserved</div>
</body>
</html>
```